Storm Restoration Contractor needs a professional business card design

Looking for a professional business card design. Not looking for your cheapo MS Word standard ones that are readily available. Dont want it to be cookie cutter look like ones readily available online. We just recently changed our logo and want to freshen up all our documents. Our company handles restoring a property back to a pre-loss condition after a storm damages it. For example, wind, hail, flood, fire losses.

Target Market(s)

Property Owners, Homeowners, Property Owners, Commercial Property Owners, Property Management Companies, Hail and Wind Damaged Properties

Industry/Entity Type

Construction Company

Contact Information for Business Card

Brightline Facades
847-555-0193
847-555-0147 fax
www.brightlinefacades.example
info@brightlinefacades.example

Requirements
Must have
• Clean, Professional, fresh look
• Storm Restoration, Roofing, Siding, Windows
Nice to have
• If there is a way to incorporate storms that may be cool.

```html
<!DOCTYPE html>
<html lang="en">
<head>
<meta charset="utf-8">
<title>Brightline Facades — Business Card</title>
<link rel="stylesheet" href="https://fonts.googleapis.com/css2?family=Lato:wght@400;700;900&display=swap">
<style>
  :root {
    --page-bg: #ececec;
    --card-dark: #1b1b1b;
    --card-light: #ffffff;
    --brand-blue: #1a75c0;
    --ink-gray: #555a5f;
    --mark-gray: #8a8a8a;
    --service-gray: #9a9a9a;
    --map-tone: #dcdde6;
    --divider: #1b1b1b;
  }
  * { box-sizing: border-box; margin: 0; padding: 0; }
  html, body { width: 1200px; height: 586px; overflow: hidden; }
  body {
    background: var(--page-bg);
    font-family: "Lato", sans-serif;
    position: relative;
  }
  .card {
    position: absolute;
    top: 129px;
    width: 502px;
    height: 301px;
    overflow: hidden;
  }
  .card--front { left: 65px; background: var(--card-dark); }
  .card--back { left: 608px; background: var(--card-light); }

  /* Front */
  .front-brand {
    position: absolute;
    left: 0; right: 0; top: 108px;
    display: flex;
    align-items: center;
    justify-content: center;
    gap: 16px;
  }
  .front-brand__dot {
    width: 56px; height: 56px;
    border-radius: 50%;
    border: 6px solid #2c2c2c;
  }
  .front-brand__name {
    color: var(--mark-gray);
    font-weight: 900;
    font-size: 30px;
    line-height: 1;
    letter-spacing: 1px;
    text-transform: uppercase;
  }
  .services {
    position: absolute;
    left: 0; right: 0; top: 251px;
    text-align: center;
    font-size: 11px;
    font-weight: 700;
    color: var(--service-gray);
    word-spacing: 1px;
  }
  .services .sep { margin: 0 7px; }

  /* Back */
  .map-area {
    position: absolute;
    left: 44px; top: 63px;
    width: 428px; height: 208px;
    border-radius: 40px;
    background: radial-gradient(ellipse at 60% 50%, var(--map-tone) 0%, rgba(220,221,230,0.35) 60%, rgba(255,255,255,0) 100%);
  }
  .back-brand {
    position: absolute;
    left: 38px; top: 66px;
    width: 180px;
    text-align: center;
  }
  .back-brand__dot {
    width: 96px; height: 96px;
    margin: 0 auto 12px;
    border-radius: 50%;
    border: 8px solid var(--brand-blue);
  }
  .back-brand__name {
    color: var(--brand-blue);
    font-weight: 900;
    font-size: 22px;
    line-height: 1.05;
    letter-spacing: 1px;
    text-transform: uppercase;
  }
  .divider {
    position: absolute;
    left: 252px; top: 60px;
    width: 2px; height: 181px;
    background: var(--divider);
  }
  .contact {
    position: absolute;
    left: 278px; top: 77px;
  }
  .contact__name {
    color: var(--brand-blue);
    font-weight: 700;
    font-size: 18px;
    line-height: 1.2;
  }
  .contact__role {
    color: var(--ink-gray);
    font-size: 11.5px;
    margin-top: 2px;
  }
  .contact__list { list-style: none; margin-top: 24px; }
  .contact__item {
    display: flex;
    align-items: center;
    gap: 7px;
    color: var(--ink-gray);
    font-size: 13px;
    height: 26.5px;
  }
  .contact__item svg { width: 15px; height: 15px; fill: var(--brand-blue); flex: none; }
  .web-band {
    position: absolute;
    left: 0; right: 0; bottom: 0;
    height: 27px;
    background: var(--brand-blue);
    color: #fff;
    font-weight: 700;
    font-size: 12.5px;
    display: flex;
    align-items: center;
    justify-content: center;
  }
</style>
</head>
<body>
  <section class="card card--front">
    <div class="front-brand">
      <div class="front-brand__dot"></div>
      <div class="front-brand__name">Brightline<br>Facades</div>
    </div>
    <p class="services">Roofing<span class="sep">•</span>Siding<span class="sep">•</span>Windows/Doors<span class="sep">•</span>Gutters</p>
  </section>

  <section class="card card--back">
    <div class="map-area" role="img" aria-label="Faint dotted world map in the card background"></div>
    <div class="back-brand">
      <div class="back-brand__dot"></div>
      <div class="back-brand__name">Brightline<br>Facades</div>
    </div>
    <div class="divider"></div>
    <div class="contact">
      <h1 class="contact__name">Daniel Marsh</h1>
      <p class="contact__role">Owner / Founder</p>
      <ul class="contact__list">
        <li class="contact__item">
          <svg viewBox="0 0 16 16" aria-hidden="true"><path d="M1 5c0-2 2-3 7-3s7 1 7 3v1h-4V4.5H5V6H1z"/><path d="M3 7h10l1.5 7h-13z"/></svg>
          847-555-0193
        </li>
        <li class="contact__item">
          <svg viewBox="0 0 16 16" aria-hidden="true"><path d="M4 1h8v4H4z"/><path d="M1 6h14v6h-3v-2H4v2H1z"/><path d="M5 11h6v4H5z"/></svg>
          847-555-0147
        </li>
        <li class="contact__item">
          <svg viewBox="0 0 16 16" aria-hidden="true"><path d="M1 3h14v10H1zm1.5 1.5v.3L8 9l5.5-4.2v-.3zM2.5 6.6v4.9h11V6.6L8 10.8z"/></svg>
          info@brightlinefacades.example
        </li>
      </ul>
    </div>
    <div class="web-band">www.brightlinefacades.example</div>
  </section>
</body>
</html>
```